45:35:20 Phase 2

This project was set up because of a problem in administering an earlier project and it is the only way we can continue to receive designs and pay the current designer.

That is why no details have been provided.

Unfortunately we cannot accept work from anyone else at this stage.

```html
<!DOCTYPE html>
<html lang="en">
<head>
<meta charset="utf-8">
<title>45:35:20 Cards</title>
<link href="https://fonts.googleapis.com/css2?family=Orbitron:wght@700&display=swap" rel="stylesheet">
<style>
  :root {
    --bg-centre: #454545;
    --bg-edge: #1c1c1c;
    --red: #d23a34;
    --red-light: #f07a5e;
    --blue: #2d6cc2;
    --blue-light: #78b6df;
    --green: #45a13a;
    --green-light: #a9d96c;
    --orange: #ec7a1c;
    --orange-light: #ffd47c;
    --frame: rgba(255, 255, 255, 0.38);
    --ink-cool: rgba(255, 255, 255, 0.45);
    --ink-green: rgba(232, 255, 180, 0.6);
    --ink-warm: rgba(255, 236, 170, 0.7);
  }
  html, body {
    margin: 0;
    padding: 0;
    width: 1200px;
    height: 1000px;
    overflow: hidden;
    background: var(--bg-edge);
  }
  .canvas {
    position: relative;
    width: 1200px;
    height: 1000px;
    background: radial-gradient(ellipse at 50% 45%, var(--bg-centre) 0%, #2a2a2a 55%, var(--bg-edge) 100%);
    font-family: "Orbitron", sans-serif;
  }
  .card {
    position: absolute;
    width: 378px;
    height: 272px;
    border-radius: 14px;
    overflow: hidden;
    box-shadow: 0 6px 18px rgba(0, 0, 0, 0.55);
  }
  .card-art {
    position: absolute;
    inset: 0;
  }
  .card-frame {
    position: absolute;
    inset: 14px;
    border: 2px solid var(--frame);
    border-radius: 12px;
  }
  .card-value {
    position: absolute;
    inset: 0;
    display: flex;
    align-items: center;
    justify-content: center;
    font-weight: 700;
    line-height: 1;
    white-space: nowrap;
  }
  .card-surprise { left: 102px; top: 325px; z-index: 2; }
  .card-twenty   { left: 410px; top: 226px; z-index: 3; }
  .card-thirty   { left: 720px; top: 325px; z-index: 1; }
  .card-fortyfive{ left: 410px; top: 522px; z-index: 4; }

  .card-surprise .card-art { background: radial-gradient(circle at 50% 50%, var(--red-light) 0%, var(--red) 72%); }
  .card-twenty .card-art   { background: radial-gradient(circle at 55% 48%, var(--blue-light) 0%, var(--blue) 72%); }
  .card-thirty .card-art   { background: radial-gradient(circle at 50% 50%, var(--green-light) 0%, var(--green) 72%); }
  .card-fortyfive .card-art{ background: radial-gradient(circle at 50% 50%, var(--orange-light) 0%, var(--orange) 72%); }

  .card-surprise .card-value { font-size: 34px; color: var(--ink-cool); }
  .card-twenty .card-value   { font-size: 56px; color: var(--ink-cool); }
  .card-thirty .card-value   { font-size: 56px; color: var(--ink-green); }
  .card-fortyfive .card-value{ font-size: 56px; color: var(--ink-warm); }
</style>
</head>
<body>
<main class="canvas">

  <section class="card card-surprise">
    <div class="card-art" role="img" aria-label="Red sunburst background scattered with exclamations such as oops, yikes and uh-oh"></div>
    <div class="card-frame"></div>
    <p class="card-value">SURPRISE</p>
  </section>

  <section class="card card-twenty">
    <div class="card-art" role="img" aria-label="Blue sunburst background scattered with repeated percentages and question marks"></div>
    <div class="card-frame"></div>
    <p class="card-value">20%</p>
  </section>

  <section class="card card-thirty">
    <div class="card-art" role="img" aria-label="Green sunburst background scattered with repeated percentages and question marks"></div>
    <div class="card-frame"></div>
    <p class="card-value">35%</p>
  </section>

  <section class="card card-fortyfive">
    <div class="card-art" role="img" aria-label="Orange sunburst background scattered with repeated percentages and question marks"></div>
    <div class="card-frame"></div>
    <p class="card-value">45%</p>
  </section>

</main>
</body>
</html>
```